you will use Ai to Copy the website Quellabyx.com to come up with the basic frame work and it will give you the understanding of how I would like Zandoprik.com to be like. Zandoprik.com is a peer to peer rv rental site very similar to both of the other rv rental sites the difference is that are commission based 20% and above per rental and we will be one flat monthly rate and they keep all the earnings. Below is photo that will help you with the color scheme and the look and feel of the design

```html
<!DOCTYPE html>
<html lang="en">
<head>
<meta charset="utf-8">
<title>Zandoprik — Peer-to-peer RV rentals</title>
<link href="https://fonts.googleapis.com/css2?family=Playfair+Display:wght@600;700&family=Inter:wght@400;500;600;700&display=swap" rel="stylesheet">
<style>
:root{
  --green:#3d7d1f;
  --green-dark:#2f6517;
  --green-light:#8cc63f;
  --green-tint:#eaf3e1;
  --navy:#15203a;
  --navy-deep:#111a30;
  --cream:#faf5ea;
  --gold:#e29a2d;
  --ink:#1d2433;
  --muted:#6b7280;
  --line:#e6e3dc;
  --white:#ffffff;
}
*{box-sizing:border-box;margin:0;padding:0}
html,body{width:1200px;height:4129px;overflow:hidden}
body{font-family:"Inter",sans-serif;color:var(--ink);background:var(--white);font-size:11px}
.serif{font-family:"Playfair Display",serif}
.wrap{padding:0 50px;position:relative}
.eyebrow{font-size:8px;font-weight:700;letter-spacing:.12em;text-transform:uppercase;color:var(--green)}
.h2{font-family:"Playfair Display",serif;font-weight:600;font-size:27px;color:var(--ink);margin-top:8px}
.btn{display:inline-flex;align-items:center;gap:6px;border-radius:6px;font-weight:600;font-size:10px;height:34px;padding:0 16px}
.btn-green{background:var(--green);color:#fff}
.btn-outline{border:1px solid #c9c9c9;color:var(--ink);background:#fff}

/* nav */
.nav{height:42px;display:flex;align-items:center;padding:0 38px;border-bottom:1px solid var(--line);position:relative}
.logo{display:flex;align-items:center;gap:6px;font-family:"Playfair Display",serif;font-weight:700;font-size:15px;color:var(--green)}
.logo i{width:9px;height:9px;border-radius:50%;background:var(--green)}
.nav-links{position:absolute;left:431px;display:flex;gap:20px;font-size:9.5px;color:#374151}
.nav-right{margin-left:auto;display:flex;gap:8px}
.nav-right .btn{height:24px;font-size:9px;padding:0 12px;border-radius:5px}

/* hero */
.hero{height:472px;position:relative;overflow:hidden;color:#fff}
.hero-bg{position:absolute;inset:0;background:
  radial-gradient(ellipse 420px 260px at 62% 62%,rgba(238,150,70,.55),transparent 70%),
  radial-gradient(ellipse 300px 200px at 80% 45%,rgba(200,210,230,.35),transparent 70%),
  linear-gradient(90deg,#0c1424 0%,#1a2436 35%,#3a3a3c 60%,#2a2f2f 80%,#18211c 100%)}
.hero-rv{position:absolute;left:650px;top:180px;width:340px;height:190px;border-radius:30px 60px 14px 14px;background:linear-gradient(180deg,#ecece6 0%,#d8d8d0 55%,#4b7d2a 56%,#3a6a20 75%,#222 100%);opacity:.9}
.hero-road{position:absolute;left:430px;bottom:0;width:520px;height:120px;background:linear-gradient(180deg,rgba(30,30,34,0),#1b1d22);clip-path:polygon(40% 0,60% 0,100% 100%,0 100%)}
.hero-content{position:absolute;left:50px;top:59px;width:380px}
.badge{display:inline-flex;align-items:center;gap:6px;height:18px;padding:0 10px;border-radius:9px;background:rgba(140,198,63,.18);border:1px solid rgba(140,198,63,.45);color:#b9e07d;font-size:7px;font-weight:700;letter-spacing:.1em}
.badge i{width:4px;height:4px;border-radius:50%;background:var(--green-light)}
.hero h1{font-family:"Playfair Display",serif;font-weight:700;font-size:39px;line-height:43px;margin-top:16px}
.hero h1 em{font-style:normal;color:var(--green-light)}
.hero p{font-size:10.5px;line-height:18px;color:#d6d9df;margin-top:16px;width:320px}
.hero-ctas{display:flex;gap:10px;margin-top:30px}
.hero-ctas .btn-ghost{border:1px solid rgba(255,255,255,.6);color:#fff}
.stats{display:flex;gap:30px;margin-top:62px}
.stat b{display:block;font-family:"Playfair Display",serif;font-size:18px;font-weight:600}
.stat span{font-size:6.5px;letter-spacing:.1em;color:#a9aebb}

/* search */
.search-band{height:76px;padding:16px 50px 0}
.search{height:42px;border:1px solid var(--line);border-radius:8px;display:flex;align-items:center;box-shadow:0 2px 8px rgba(0,0,0,.05)}
.field{flex:1;padding:0 14px;border-right:1px solid var(--line);height:28px;display:flex;flex-direction:column;justify-content:center}
.field:nth-child(4){border-right:0;flex:1.05}
.field label{font-size:6.5px;font-weight:700;letter-spacing:.08em;color:#333}
.field span{font-size:9px;color:#9ca3af;margin-top:3px;display:flex;justify-content:space-between}
.search .btn{height:30px;border-radius:15px;margin-right:6px;padding:0 18px;font-size:9px}

/* process */
.process{height:349px;background:var(--cream);padding-top:45px}
.steps{display:grid;grid-template-columns:repeat(3,1fr);gap:18px;margin-top:28px}
.step{background:#fff;border:1px solid #efe8d8;border-radius:8px;height:181px;padding:22px 20px}
.step .num{font-family:"Playfair Display",serif;font-size:28px;color:#e8dfc9;line-height:1}
.icon-box{width:28px;height:28px;border-radius:6px;background:var(--green-tint);display:flex;align-items:center;justify-content:center;margin-top:10px}
.step h3{font-size:11.5px;font-weight:600;margin-top:14px}
.step p{font-size:8.5px;line-height:15px;color:var(--muted);margin-top:10px}

/* listings */
.listings{height:851px;padding-top:50px}
.listings .head{display:flex;justify-content:space-between;align-items:flex-end}
.listings .head .btn{height:30px;font-size:9px}
.filters{display:flex;gap:8px;margin-top:18px}
.chip{height:19px;padding:0 12px;border:1px solid var(--line);border-radius:10px;font-size:8px;display:flex;align-items:center;color:#374151}
.chip.on{background:var(--navy);color:#fff;border-color:var(--navy)}
.grid5{display:grid;grid-template-columns:repeat(5,1fr);gap:15px;margin-top:22px}
.grid5+.grid5{margin-top:24px}
.card{border:1px solid var(--line);border-radius:8px;overflow:hidden;height:283px;position:relative;background:#fff}
.photo{height:155px;position:relative;background:linear-gradient(180deg,#2b4a7a 0%,#5f80a8 38%,#d8d8d8 55%,#3c4b3b 75%,#1f2a1f 100%)}
.photo.night{background:linear-gradient(180deg,#0e1530 0%,#22305a 40%,#ccc8be 56%,#56585a 70%,#25282c 100%)}
.photo.flat{background:var(--green);display:flex;flex-direction:column;align-items:center;justify-content:center;gap:8px;color:#fff;font-size:7px}
.tag{position:absolute;left:8px;top:8px;height:14px;padding:0 7px;border-radius:3px;font-size:6.5px;font-weight:700;display:flex;align-items:center;color:#fff}
.tag.gold{background:var(--gold)}.tag.green{background:var(--green)}.tag.navy{background:var(--navy)}
.heart{position:absolute;right:8px;top:8px;width:18px;height:18px;border-radius:50%;background:#fff;display:flex;align-items:center;justify-content:center}
.dots{position:absolute;bottom:6px;left:50%;transform:translateX(-50%);display:flex;gap:3px}
.dots i{width:3px;height:3px;border-radius:50%;background:rgba(255,255,255,.6)}.dots i:first-child{background:#fff}
.body{padding:12px 12px}
.cls{font-size:6.5px;font-weight:700;letter-spacing:.08em;color:var(--green);text-transform:uppercase}
.card h4{font-size:9px;font-weight:700;line-height:12px;margin-top:5px;height:24px}
.loc{font-size:7.5px;color:var(--muted);margin-top:3px}
.feat{font-size:7px;color:var(--muted);margin-top:6px;display:flex;gap:8px}
.feat b{color:var(--gold);font-weight:400}
.price{position:absolute;left:12px;right:12px;bottom:14px;display:flex;justify-content:space-between;align-items:baseline}
.price strong{font-size:14px;font-weight:700}
.price strong small{font-size:7.5px;color:var(--muted);font-weight:400}
.rate{font-size:7.5px;font-weight:600}.rate i{font-style:normal;color:var(--gold)}.rate span{color:var(--muted);font-weight:400}
.more{display:flex;justify-content:center;margin-top:29px}
.more .btn{height:30px;font-size:9px;border-color:#555}

/* destinations */
.dest{height:517px;background:var(--navy);padding-top:50px;color:#fff}
.dest .eyebrow{color:var(--green-light)}
.dest .h2{color:#fff}
.dest .sub{font-size:9.5px;color:#b5bccb;line-height:18px;margin-top:8px;width:300px}
.view-all{position:absolute;right:50px;top:78px;font-size:8.5px;font-weight:600;color:var(--green-light)}
.dest-grid{display:grid;grid-template-columns:541px 271px 270px;grid-template-rows:148px 148px;gap:9px 8px;margin-top:18px}
.tile{position:relative;border-radius:4px;overflow:hidden}
.tile.big{grid-row:1/3}
.tile .cap{position:absolute;left:14px;bottom:14px}
.tile .cap b{font-family:"Playfair Display",serif;font-size:13px;font-weight:600;display:block}
.tile .cap span{font-size:7px;color:#d8dce4}
.tile.big .cap{left:14px;bottom:16px}
.tile.big .cap b{font-size:17px;margin-top:6px}
.np{display:inline-block;background:var(--green);font-size:6px;font-weight:700;letter-spacing:.1em;padding:3px 6px;border-radius:2px}

/* earn */
.earn{height:352px;background:var(--cream);padding-top:50px}
.earn h2{font-family:"Playfair Display",serif;font-weight:700;font-size:30px;margin-top:8px}
.earn h2 em{font-style:normal;color:var(--gold)}
.earn .lead{font-size:9.5px;color:var(--muted);margin-top:4px}
.perks{margin-top:22px;display:flex;flex-direction:column;gap:16px;width:330px}
.perk{display:flex;gap:12px}
.perk .ic{width:20px;height:20px;border-radius:50%;background:#f6e4c4;flex:none;display:flex;align-items:center;justify-content:center}
.perk b{font-size:9px;display:block}
.perk span{font-size:7.5px;color:var(--muted);display:block;margin-top:4px}
.earn .btn{margin-top:22px;height:34px}
.income{position:absolute;left:575px;top:4px;width:524px;height:242px;background:#fff;border-radius:8px;box-shadow:0 4px 18px rgba(0,0,0,.08);padding:22px 18px}
.income h5{font-size:9px;font-weight:600}
.bars{margin-top:12px;display:flex;flex-direction:column;gap:9px}
.bar{display:flex;align-items:center;gap:8px;font-size:7px;color:var(--muted)}
.bar .m{width:26px;text-align:right}
.track{flex:1;height:14px;background:#f2f2f0;border-radius:3px}
.fill{height:14px;background:var(--green);border-radius:3px;color:#fff;font-size:7px;font-weight:700;padding-left:6px;line-height:14px}
.total{position:absolute;left:18px;right:18px;bottom:22px;border-top:1px solid var(--line);padding-top:14px;display:flex;justify-content:space-between;align-items:flex-end}
.total span{font-size:7.5px;color:var(--muted);line-height:11px}
.total b{font-family:"Playfair Display",serif;font-size:20px;color:var(--green);font-weight:700}

/* lists */
.cities{height:305px;padding-top:48px}
.states{height:448px;padding-top:48px}
.cols{display:grid;grid-template-columns:repeat(8,1fr);row-gap:17px;margin-top:22px}
.cols div b{display:block;font-size:8.5px;font-weight:500}
.cols div span{display:block;font-size:6.5px;color:var(--muted);margin-top:3px}
.states .cols{row-gap:17px;margin-top:22px}

/* reviews */
.reviews{height:305px;padding-top:42px}
.score{position:absolute;right:50px;top:40px;display:flex;align-items:center;gap:8px}
.score b{font-family:"Playfair Display",serif;font-size:24px;font-weight:600}
.score span{font-size:7px;color:var(--muted);line-height:10px}
.score i{font-style:normal;color:var(--gold);font-size:8px;letter-spacing:1px}
.revs{display:grid;grid-template-columns:repeat(3,1fr);gap:18px;margin-top:22px}
.rev{border:1px solid var(--line);border-radius:8px;height:144px;padding:16px 18px}
.rev .st{color:var(--gold);font-size:8px;letter-spacing:2px}
.rev p{font-size:8px;font-style:italic;color:#4b5563;line-height:15px;margin-top:8px}
.who{display:flex;gap:8px;align-items:center;margin-top:12px}
.av{width:22px;height:22px;border-radius:50%;color:#fff;font-size:7px;font-weight:700;display:flex;align-items:center;justify-content:center}
.who b{font-size:8px;display:block}.who span{font-size:6.5px;color:var(--muted)}

/* cta */
.cta{height:179px;background:var(--navy);color:#fff;padding-top:56px}
.cta h2{font-family:"Playfair Display",serif;font-weight:600;font-size:22px;line-height:26px}
.cta h2 em{font-style:normal;color:var(--green-light)}
.cta-side{position:absolute;right:50px;top:4px;text-align:center}
.cta-side .btn{height:35px;padding:0 22px}
.cta-side span{display:block;font-size:7px;color:#8c95a8;margin-top:10px}

/* footer */
.foot{height:233px;background:var(--navy-deep);color:#c3c9d6;padding-top:40px;position:relative}
.foot .logo{color:#fff;font-size:14px}.foot .logo i{background:var(--green-light)}
.foot .about{font-size:7.5px;line-height:13px;color:#8c95a8;margin-top:14px;width:180px}
.social{display:flex;gap:6px;margin-top:12px}
.social i{width:16px;height:16px;border-radius:50%;border:1px solid #3a4560}
.fcols{position:absolute;top:0;left:433px;display:flex;gap:0}
.fcol{width:232px}
.fcol h6{font-size:6.5px;font-weight:700;letter-spacing:.1em;color:#fff}
.fcol a{display:block;font-size:7.5px;color:#8c95a8;margin-top:9px;text-decoration:none}
.fbottom{position:absolute;left:50px;right:50px;bottom:12px;border-top:1px solid #26304a;padding-top:12px;display:flex;justify-content:space-between;font-size:6.5px;color:#6f7890}
.fbottom div{display:flex;gap:14px}
</style>
</head>
<body>

<header class="nav">
  <div class="logo"><i></i>Zandoprik</div>
  <nav class="nav-links"><span>Browse RVs</span><span>Destinations</span><span>How it works</span><span>List your RV</span></nav>
  <div class="nav-right"><span class="btn btn-outline">Sign in</span><span class="btn btn-green">List your RV →</span></div>
</header>

<section class="hero">
  <div class="hero-bg" role="img" aria-label="Class C motorhome driving a forest road toward snowy mountains at sunset"></div>
  <div class="hero-content">
    <span class="badge"><i></i>AMERICA'S #1 PEER-TO-PEER RV MARKETPLACE</span>
    <h1>Your next road<br>trip starts <em>right<br>here</em></h1>
    <p>Rent a private RV from real owners nationwide — or list yours and start earning while it sits in the driveway.</p>
    <div class="hero-ctas"><span class="btn btn-green">Browse RVs near me</span><span class="btn btn-ghost">List your RV →</span></div>
    <div class="stats">
      <div class="stat"><b>12,400+</b><span>RVS LISTED</span></div>
      <div class="stat"><b>48</b><span>STATES COVERED</span></div>
      <div class="stat"><b>4.9★</b><span>AVG. RATING</span></div>
    </div>
  </div>
</section>

<div class="search-band">
  <div class="search">
    <div class="field"><label>WHERE</label><span>City, state, or zip code</span></div>
    <div class="field"><label>PICK-UP DATE</label><span>Add date</span></div>
    <div class="field"><label>RETURN DATE</label><span>Add date</span></div>
    <div class="field"><label>RV TYPE</label><span>All types <em style="font-style:normal;color:#333">⌄</em></span></div>
    <span class="btn btn-green"><svg width="9" height="9" viewBox="0 0 10 10" fill="none" stroke="#fff" stroke-width="1.4"><circle cx="4.2" cy="4.2" r="3.2"/><path d="M6.6 6.6 9 9"/></svg>Search</span>
  </div>
</div>

<section class="process">
  <div class="wrap">
    <div class="eyebrow">Simple process</div>
    <h2 class="h2">Renting an RV has never been easier</h2>
    <div class="steps">
      <div class="step"><div class="num">01</div>
        <div class="icon-box"><svg width="12" height="12" viewBox="0 0 12 12" fill="none" stroke="#3d7d1f" stroke-width="1.4"><circle cx="5" cy="5" r="3.5"/><path d="m7.6 7.6 3 3"/></svg></div>
        <h3>Find your perfect RV</h3><p>Search thousands of RVs by location, dates, type, and budget. Filter by sleeps, pet-friendly, delivery, and more.</p></div>
      <div class="step"><div class="num">02</div>
        <div class="icon-box"><svg width="12" height="12" viewBox="0 0 12 12" fill="none" stroke="#3d7d1f" stroke-width="1.4"><path d="M6 1 10 2.6v3C10 8.4 8.2 10.2 6 11 3.8 10.2 2 8.4 2 5.6v-3Z"/></svg></div>
        <h3>Book with confidence</h3><p>Secure payment, verified owners, and $1M insurance coverage on every trip. Message the host before you commit.</p></div>
      <div class="step"><div class="num">03</div>
        <div class="icon-box"><svg width="12" height="12" viewBox="0 0 12 12" fill="none" stroke="#3d7d1f" stroke-width="1.4"><path d="M1.5 5.5 6 1.5l4.5 4V10.5h-9Z"/><path d="M4.5 10.5V7.5h3v3"/></svg></div>
        <h3>Hit the open road</h3><p>Pick up your RV (or have it delivered), make memories, and return it when the adventure wraps up.</p></div>
    </div>
  </div>
</section>

<section class="listings">
  <div class="wrap">
    <div class="head">
      <div><div class="eyebrow">Available near you</div><h2 class="h2">Top-rated RVs to rent</h2></div>
      <span class="btn btn-outline">View all listings →</span>
    </div>
    <div class="filters">
      <span class="chip on">All types</span><span class="chip">Class A</span><span class="chip">Campervans</span><span class="chip">Travel trailers</span><span class="chip">Fifth wheels</span><span class="chip">Pet friendly</span><span class="chip">Delivery available</span>
    </div>

    <div class="grid5">
      <article class="card"><div class="photo" role="img" aria-label="Class A motorhome parked by mountains"><span class="tag gold">Top rated</span><span class="heart"><svg width="9" height="8" viewBox="0 0 10 9" fill="none" stroke="#555" stroke-width="1.1"><path d="M5 8.2 1.3 4.6A2.2 2.2 0 0 1 5 1.8a2.2 2.2 0 0 1 3.7 2.8Z"/></svg></span><span class="dots"><i></i><i></i><i></i></span></div>
        <div class="body"><div class="cls">Class A Motorhome</div><h4>2022 Torvane Palisade — Luxury King Suite</h4><div class="loc">◎ Denver, CO</div><div class="feat"><span>Sleeps 6</span><span>40 ft</span><span>Pet friendly</span></div></div>
        <div class="price"><strong>$295<small>/night</small></strong><span class="rate"><i>★</i> 4.98 <span>(124)</span></span></div></article>
      <article class="card"><div class="photo night" role="img" aria-label="Campervan under a starry night sky"><span class="tag green">Delivery</span><span class="heart"><svg width="9" height="8" viewBox="0 0 10 9" fill="none" stroke="#555" stroke-width="1.1"><path d="M5 8.2 1.3 4.6A2.2 2.2 0 0 1 5 1.8a2.2 2.2 0 0 1 3.7 2.8Z"/></svg></span><span class="dots"><i></i><i></i><i></i></span></div>
        <div class="body"><div class="cls">Class B Campervan</div><h4>2023 Meridane Strider — Off-Grid Build</h4><div class="loc">◎ Austin, TX</div><div class="feat"><span>Sleeps 2</span><span><b>●</b> Solar</span><span>Skylinq</span></div></div>
        <div class="price"><strong>$145<small>/night</small></strong><span class="rate"><i>★</i> 5.0 <span>(89)</span></span></div></article>
      <article class="card"><div class="photo" role="img" aria-label="Travel trailer parked in mountain landscape"><span class="heart"><svg width="9" height="8" viewBox="0 0 10 9" fill="none" stroke="#555" stroke-width="1.1"><path d="M5 8.2 1.3 4.6A2.2 2.2 0 0 1 5 1.8a2.2 2.2 0 0 1 3.7 2.8Z"/></svg></span><span class="dots"><i></i><i></i><i></i></span></div>
        <div class="body"><div class="cls">Travel Trailer</div><h4>2021 Aerolune Bramble 16RB — Classic Aluminum</h4><div class="loc">◎ Portland, OR</div><div class="feat"><span>Sleeps 2</span><span>Full kitchen</span></div></div>
        <div class="price"><strong>$175<small>/night</small></strong><span class="rate"><i>★</i> 4.95 <span>(67)</span></span></div></article>
      <article class="card"><div class="photo night" role="img" aria-label="Family motorhome at night under stars"><span class="tag navy">New listing</span><span class="heart"><svg width="9" height="8" viewBox="0 0 10 9" fill="none" stroke="#555" stroke-width="1.1"><path d="M5 8.2 1.3 4.6A2.2 2.2 0 0 1 5 1.8a2.2 2.2 0 0 1 3.7 2.8Z"/></svg></span><span class="dots"><i></i><i></i><i></i></span></div>
        <div class="body"><div class="cls">Class A Motorhome</div><h4>2020 Wendaro Adventurist — Family Ready</h4><div class="loc">◎ Nashville, TN</div><div class="feat"><span>Sleeps 7</span><span>Pet friendly</span><span>Delivery</span></div></div>
        <div class="price"><strong>$185<small>/night</small></strong><span class="rate"><i>★</i> 4.9 <span>(22)</span></span></div></article>
      <article class="card"><div class="photo flat" role="img" aria-label="Campervan open road placeholder"><svg width="50" height="28" viewBox="0 0 50 28" fill="none" stroke="#fff" stroke-width="2"><path d="M3 6h30l10 9v8H3Z"/><path d="M33 6v9h10"/><circle cx="12" cy="23" r="3.5" fill="#3d7d1f"/><circle cx="36" cy="23" r="3.5" fill="#3d7d1f"/></svg><span>Campervan open road</span><span class="heart"><svg width="9" height="8" viewBox="0 0 10 9" fill="none" stroke="#555" stroke-width="1.1"><path d="M5 8.2 1.3 4.6A2.2 2.2 0 0 1 5 1.8a2.2 2.2 0 0 1 3.7 2.8Z"/></svg></span><span class="dots"><i></i><i></i><i></i></span></div>
        <div class="body"><div class="cls">Fifth Wheel</div><h4>2022 Granvista Reflex 150 Series</h4><div class="loc">◎ Phoenix, AZ</div><div class="feat"><span>Sleeps 8</span><span>Full kitchen</span></div></div>
        <div class="price"><strong>$220<small>/night</small></strong><span class="rate"><i>★</i> 4.97 <span>(54)</span></span></div></article>
    </div>

    <div class="grid5">
      <article class="card"><div class="photo night" role="img" aria-label="Campervan van build at night"><span class="tag gold">Best value</span><span class="heart"><svg width="9" height="8" viewBox="0 0 10 9" fill="none" stroke="#555" stroke-width="1.1"><path d="M5 8.2 1.3 4.6A2.2 2.2 0 0 1 5 1.8a2.2 2.2 0 0 1 3.7 2.8Z"/></svg></span><span class="dots"><i></i><i></i><i></i></span></div>
        <div class="body"><div class="cls">Class B Campervan</div><h4>2019 Fordale Transito — Adventure-Ready Van Build</h4><div class="loc">◎ Atlanta, GA</div><div class="feat"><span>Sleeps 2</span><span>Pet OK</span><span>Delivery</span></div></div>
        <div class="price"><strong>$98<small>/night</small></strong><span class="rate"><i>★</i> 4.85 <span>(41)</span></span></div></article>
      <article class="card"><div class="photo" role="img" aria-label="Row of motorhomes by mountains"><span class="tag gold">Top rated</span><span class="heart"><svg width="9" height="8" viewBox="0 0 10 9" fill="none" stroke="#555" stroke-width="1.1"><path d="M5 8.2 1.3 4.6A2.2 2.2 0 0 1 5 1.8a2.2 2.2 0 0 1 3.7 2.8Z"/></svg></span><span class="dots"><i></i><i></i><i></i></span></div>
        <div class="body"><div class="cls">Class A Motorhome</div><h4>2022 Torvane Palisade — Luxury King Suite</h4><div class="loc">◎ Denver, CO</div><div class="feat"><span>Sleeps 6</span><span>40 ft</span><span>Pet friendly</span></div></div>
        <div class="price"><strong>$295<small>/night</small></strong><span class="rate"><i>★</i> 4.98 <span>(124)</span></span></div></article>
      <article class="card"><div class="photo night" role="img" aria-label="Campervan under a starry night sky"><span class="tag green">Delivery</span><span class="heart"><svg width="9" height="8" viewBox="0 0 10 9" fill="none" stroke="#555" stroke-width="1.1"><path d="M5 8.2 1.3 4.6A2.2 2.2 0 0 1 5 1.8a2.2 2.2 0 0 1 3.7 2.8Z"/></svg></span><span class="dots"><i></i><i></i><i></i></span></div>
        <div class="body"><div class="cls">Class B Campervan</div><h4>2023 Meridane Strider — Off-Grid Build</h4><div class="loc">◎ Austin, TX</div><div class="feat"><span>Sleeps 2</span><span><b>●</b> Solar</span><span>Skylinq</span></div></div>
        <div class="price"><strong>$145<small>/night</small></strong><span class="rate"><i>★</i> 5.0 <span>(89)</span></span></div></article>
      <article class="card"><div class="photo" role="img" aria-label="Travel trailers in mountain landscape"><span class="heart"><svg width="9" height="8" viewBox="0 0 10 9" fill="none" stroke="#555" stroke-width="1.1"><path d="M5 8.2 1.3 4.6A2.2 2.2 0 0 1 5 1.8a2.2 2.2 0 0 1 3.7 2.8Z"/></svg></span><span class="dots"><i></i><i></i><i></i></span></div>
        <div class="body"><div class="cls">Travel Trailer</div><h4>2021 Aerolune Bramble 16RB — Classic Aluminum</h4><div class="loc">◎ Portland, OR</div><div class="feat"><span>Sleeps 2</span><span>Full kitchen</span></div></div>
        <div class="price"><strong>$175<small>/night</small></strong><span class="rate"><i>★</i> 4.95 <span>(67)</span></span></div></article>
      <article class="card"><div class="photo night" role="img" aria-label="Family motorhome at night under stars"><span class="tag navy">New listing</span><span class="heart"><svg width="9" height="8" viewBox="0 0 10 9" fill="none" stroke="#555" stroke-width="1.1"><path d="M5 8.2 1.3 4.6A2.2 2.2 0 0 1 5 1.8a2.2 2.2 0 0 1 3.7 2.8Z"/></svg></span><span class="dots"><i></i><i></i><i></i></span></div>
        <div class="body"><div class="cls">Class A Motorhome</div><h4>2020 Wendaro Adventurist — Family Ready</h4><div class="loc">◎ Nashville, TN</div><div class="feat"><span>Sleeps 7</span><span>Pet friendly</span><span>Delivery</span></div></div>
        <div class="price"><strong>$185<small>/night</small></strong><span class="rate"><i>★</i> 4.9 <span>(22)</span></span></div></article>
    </div>
    <div class="more"><span class="btn btn-outline">See all 12,400+ available RVs →</span></div>
  </div>
</section>

<section class="dest">
  <div class="wrap">
    <div class="eyebrow">Explore America</div>
    <h2 class="h2">Popular RV destinations</h2>
    <p class="sub">National parks, coastlines, mountains — find RVs already near where you want to go.</p>
    <span class="view-all">View all →</span>
    <div class="dest-grid">
      <div class="tile big" role="img" aria-label="Yellowstone hot spring under a blue sky" style="background:linear-gradient(180deg,#3f6fb0 0%,#9cb8d8 35%,#6f8a6a 48%,#b9b08a 60%,#6a8a8f 75%,#3c4a3e 100%)"><div class="cap"><span class="np">NATIONAL PARK</span><b>Yellowstone</b><span>340 RVs available</span></div></div>
      <div class="tile" role="img" aria-label="Grand Canyon cliffs" style="background:linear-gradient(180deg,#7f97b4 0%,#b08867 40%,#8a4e2e 70%,#4a2a1c 100%)"><div class="cap"><b>Grand Canyon</b><span>210 RVs available</span></div></div>
      <div class="tile" role="img" aria-label="Pacific coastline with waves" style="background:linear-gradient(180deg,#8fa6c0 0%,#5d7d9c 40%,#2f5a7a 65%,#1d3346 100%)"><div class="cap"><b>Pacific Coast</b><span>512 RVs available</span></div></div>
      <div class="tile" role="img" aria-label="Sedona and Zion red rock canyon" style="background:linear-gradient(180deg,#8a98a8 0%,#9b7a62 45%,#6e4330 75%,#3a251c 100%)"><div class="cap"><b>Sedona &amp; Zion</b><span>189 RVs available</span></div></div>
      <div class="tile" role="img" aria-label="Smoky Mountains forest under clouds" style="background:linear-gradient(180deg,#c7d3dc 0%,#8fa9b6 40%,#4f7a6a 70%,#2b4a3a 100%)"><div class="cap"><b>Smoky Mountains</b><span>275 RVs available</span></div></div>
    </div>
  </div>
</section>

<section class="earn">
  <div class="wrap">
    <div class="eyebrow">For RV owners</div>
    <h2>Earn up to <em>$52,000</em></h2>
    <div class="lead">per year listing your RV on Zandoprik.com</div>
    <div class="perks">
      <div class="perk"><span class="ic"><svg width="9" height="9" viewBox="0 0 12 12" fill="none" stroke="#e29a2d" stroke-width="1.4"><path d="M6 1 10 2.6v3C10 8.4 8.2 10.2 6 11 3.8 10.2 2 8.4 2 5.6v-3Z"/></svg></span><div><b>$1M liability protection on every rental</b><span>Your RV is fully insured when it's out with a renter.</span></div></div>
      <div class="perk"><span class="ic"><svg width="9" height="9" viewBox="0 0 12 12" fill="none" stroke="#e29a2d" stroke-width="1.4"><circle cx="6" cy="6" r="4.5"/><path d="M6 3.5V6l1.8 1.2"/></svg></span><div><b>You set the schedule and price</b><span>Block dates you need, set your nightly rate, approve renters.</span></div></div>
      <div class="perk"><span class="ic"><svg width="9" height="9" viewBox="0 0 12 12" fill="none" stroke="#e29a2d" stroke-width="1.4"><rect x="1.5" y="3" width="9" height="6.5" rx="1"/><path d="M1.5 5.5h9"/></svg></span><div><b>Weekly direct deposits, every time</b><span>Get paid to your bank account the week after each rental.</span></div></div>
    </div>
    <span class="btn btn-green">Start earning — list free →</span>

    <div class="income">
      <h5>Estimated monthly income</h5>
      <div class="bars">
        <div class="bar"><span class="m">Jan</span><div class="track"><div class="fill" style="width:44%">$1,800</div></div></div>
        <div class="bar"><span class="m">Mar</span><div class="track"><div class="fill" style="width:61%">$2,480</div></div></div>
        <div class="bar"><span class="m">May</span><div class="track"><div class="fill" style="width:88%">$3,520</div></div></div>
        <div class="bar"><span class="m">Jul</span><div class="track"><div class="fill" style="width:100%">$4,300</div></div></div>
        <div class="bar"><span class="m">Sep</span><div class="track"><div class="fill" style="width:78%">$3,120</div></div></div>
        <div class="bar"><span class="m">Nov</span><div class="track"><div class="fill" style="width:38%">$1,520</div></div></div>
      </div>
      <div class="total"><span>Annual estimate<br>Class A · 30% occupancy</span><b>$28,640</b></div>
    </div>
  </div>
</section>

<section class="cities">
  <div class="wrap">
    <h2 class="h2" style="margin-top:0">Popular RV rental destinations</h2>
    <div class="cols">
      <div><b>Atlanta, GA</b><span>751 RV rentals</span></div><div><b>Austin, TX</b><span>783 RV rentals</span></div><div><b>Boston, MA</b><span>201 RV rentals</span></div><div><b>Chicago, IL</b><span>455 RV rentals</span></div><div><b>Columbus, OH</b><span>410 RV rentals</span></div><div><b>Dallas, TX</b><span>715 RV rentals</span></div><div><b>Denver, CO</b><span>1,278 RV rentals</span></div><div><b>Honolulu, HI</b><span>312 RV rentals</span></div>
      <div><b>Houston, TX</b><span>567 RV rentals</span></div><div><b>Kailua-Kona, HI</b><span>148 RV rentals</span></div><div><b>Kauai, HI</b><span>83 RV rentals</span></div><div><b>Las Vegas, NV</b><span>436 RV rentals</span></div><div><b>Los Angeles, CA</b><span>2,834 RV rentals</span></div><div><b>Maui, HI</b><span>149 RV rentals</span></div><div><b>Miami, FL</b><span>483 RV rentals</span></div><div><b>Minneapolis, MN</b><span>432 RV rentals</span></div>
      <div><b>Nashville, TN</b><span>311 RV rentals</span></div><div><b>New York, NY</b><span>575 RV rentals</span></div><div><b>Oklahoma City, OK</b><span>139 RV rentals</span></div><div><b>Orlando, FL</b><span>1,326 RV rentals</span></div><div><b>Phoenix, AZ</b><span>953 RV rentals</span></div><div><b>Portland, OR</b><span>645 RV rentals</span></div><div><b>Raleigh, NC</b><span>259 RV rentals</span></div><div><b>Salt Lake City, UT</b><span>857 RV rentals</span></div>
      <div><b>San Antonio, TX</b><span>690 RV rentals</span></div><div><b>San Diego, CA</b><span>2,093 RV rentals</span></div><div><b>San Francisco, CA</b><span>1,447 RV rentals</span></div><div><b>Seattle, WA</b><span>790 RV rentals</span></div>
    </div>
  </div>
</section>

<section class="states">
  <div class="wrap">
    <h2 class="h2" style="margin-top:0">Search RVs by state</h2>
    <div class="cols">
      <div><b>Alabama</b><span>516 RV rentals</span></div><div><b>Alaska</b><span>859 RV rentals</span></div><div><b>Arizona</b><span>1,144 RV rentals</span></div><div><b>Arkansas</b><span>86 RV rentals</span></div><div><b>California</b><span>6,292 RV rentals</span></div><div><b>Colorado</b><span>1,485 RV rentals</span></div><div><b>Connecticut</b><span>451 RV rentals</span></div><div><b>Delaware</b><span>463 RV rentals</span></div>
      <div><b>Florida</b><span>2,453 RV rentals</span></div><div><b>Georgia</b><span>1,029 RV rentals</span></div><div><b>Hawaii</b><span>433 RV rentals</span></div><div><b>Idaho</b><span>632 RV rentals</span></div><div><b>Illinois</b><span>114 RV rentals</span></div><div><b>Indiana</b><span>242 RV rentals</span></div><div><b>Iowa</b><span>106 RV rentals</span></div><div><b>Kansas</b><span>148 RV rentals</span></div>
      <div><b>Kentucky</b><span>205 RV rentals</span></div><div><b>Louisiana</b><span>269 RV rentals</span></div><div><b>Maine</b><span>53 RV rentals</span></div><div><b>Maryland</b><span>639 RV rentals</span></div><div><b>Massachusetts</b><span>369 RV rentals</span></div><div><b>Michigan</b><span>1,292 RV rentals</span></div><div><b>Minnesota</b><span>597 RV rentals</span></div><div><b>Mississippi</b><span>39 RV rentals</span></div>
      <div><b>Missouri</b><span>453 RV rentals</span></div><div><b>Montana</b><span>266 RV rentals</span></div><div><b>Nebraska</b><span>60 RV rentals</span></div><div><b>Nevada</b><span>1,029 RV rentals</span></div><div><b>New Hampshire</b><span>333 RV rentals</span></div><div><b>New Jersey</b><span>587 RV rentals</span></div><div><b>New Mexico</b><span>181 RV rentals</span></div><div><b>New York</b><span>186 RV rentals</span></div>
      <div><b>North Carolina</b><span>1,169 RV rentals</span></div><div><b>North Dakota</b><span>55 RV rentals</span></div><div><b>Ohio</b><span>458 RV rentals</span></div><div><b>Oklahoma</b><span>273 RV rentals</span></div><div><b>Oregon</b><span>1,051 RV rentals</span></div><div><b>Pennsylvania</b><span>250 RV rentals</span></div><div><b>Rhode Island</b><span>350 RV rentals</span></div><div><b>South Carolina</b><span>290 RV rentals</span></div>
      <div><b>South Dakota</b><span>73 RV rentals</span></div><div><b>Tennessee</b><span>626 RV rentals</span></div><div><b>Texas</b><span>2,651 RV rentals</span></div><div><b>Utah</b><span>1,039 RV rentals</span></div><div><b>Vermont</b><span>315 RV rentals</span></div><div><b>Virginia</b><span>635 RV rentals</span></div><div><b>Washington</b><span>681 RV rentals</span></div><div><b>Washington, DC</b><span>584 RV rentals</span></div>
      <div><b>West Virginia</b><span>220 RV rentals</span></div><div><b>Wisconsin</b><span>367 RV rentals</span></div><div><b>Wyoming</b><span>87 RV rentals</span></div>
    </div>
  </div>
</section>

<section class="reviews">
  <div class="wrap">
    <div class="eyebrow">Real renters</div>
    <h2 class="h2">What our community says</h2>
    <div class="score"><b>4.9</b><span><i>★★★★★</i><br>18,400+ reviews</span></div>
    <div class="revs">
      <div class="rev"><div class="st">★★★★★</div><p>"We rented a Class C for a 10-day Yellowstone trip with our three kids. The host was incredibly helpful, the RV was spotless, and the whole booking was seamless. Already planning our next trip!"</p>
        <div class="who"><span class="av" style="background:var(--navy)">ML</span><div><b>Marnie L.</b><span>Boulder, CO · Rented Class C Motorhome</span></div></div></div>
      <div class="rev"><div class="st">★★★★★</div><p>"First-time RV renter here — the host walked me through everything. The campervan was a dream: solar panels, satellite WiFi, memory foam bed. This is how travel should feel."</p>
        <div class="who"><span class="av" style="background:var(--green)">TW</span><div><b>Tobin W.</b><span>Chicago, IL · Rented Class B Campervan</span></div></div></div>
      <div class="rev"><div class="st">★★★★★</div><p>"Listed our Aerolune three months ago and it's already paid for itself twice over. The platform handles insurance, payments, and messaging. Highly recommend to any RV owner."</p>
        <div class="who"><span class="av" style="background:var(--gold)">EP</span><div><b>Elsa P.</b><span>Sedona, AZ · RV Host since 2023</span></div></div></div>
    </div>
  </div>
</section>

<section class="cta">
  <div class="wrap">
    <h2>Your driveway parked RV<br>could be earning <em>real money</em><br>this weekend.</h2>
    <div class="cta-side"><span class="btn btn-green">List your RV — it's free →</span><span>No commitment. Cancel anytime.</span></div>
  </div>
</section>

<footer class="foot">
  <div class="wrap">
    <div class="logo"><i></i>Zandoprik</div>
    <p class="about">The peer-to-peer RV marketplace connecting adventurers with owners across all 48 states. List it. Rent it. Bank it.</p>
    <div class="social"><i></i><i></i><i></i><i></i></div>
    <div class="fcols">
      <div class="fcol"><h6>FOR RENTERS</h6><a>Browse all RVs</a><a>RV types guide</a><a>Destinations</a><a>Renter protection</a><a>FAQ</a></div>
      <div class="fcol"><h6>FOR OWNERS</h6><a>List your RV</a><a>How pricing works</a><a>Host protection</a><a>Earnings calculator</a><a>Host resources</a></div>
      <div class="fcol"><h6>COMPANY</h6><a>About us</a><a>Careers</a><a>Press</a><a>Blog</a><a>Contact</a></div>
    </div>
  </div>
  <div class="fbottom"><span>© 2024 Zandoprik.com · All rights reserved</span><div><span>Privacy policy</span><span>Terms of service</span><span>Sitemap</span></div></div>
</footer>

</body>
</html>
```